Business Card Design

We need a business card to highlight our property maintenance company. we specialize in commercial and industrial property maintenance. services include landscaping snow and ice management. janitorial services. cleanroom services. parking lot maintenance.
Updates
I have narrowed down to two designs thank you waiting on some minor changes to both designs to choose.
Target Market(s)
facility managers/property managers
Industry/Entity Type
Property Maintenance
Contact Information for Business Card
47 Brindlewood Rd.
Harlow Falls, MA. 01839
978-552-3716
Look and feel

```html
<!DOCTYPE html>
<html lang="en">
<head>
<meta charset="utf-8">
<title>Keystone Property Maintenance – Business Card</title>
<link rel="stylesheet" href="https://fonts.googleapis.com/css2?family=Exo+2:wght@400;600;800&display=swap">
<style>
  :root {
    --bg: #d9d9d9;
    --card: #ffffff;
    --navy: #2b2a3b;
    --yellow: #f6c324;
    --ink: #1f1f26;
    --muted: #55555f;
    --light: #ffffff;
  }
  * { box-sizing: border-box; margin: 0; padding: 0; }
  html, body { width: 1200px; height: 949px; overflow: hidden; }
  body {
    background: var(--bg);
    font-family: "Exo 2", sans-serif;
    position: relative;
  }
  .card {
    position: absolute;
    left: 250px;
    width: 700px;
    height: 400px;
    background: var(--card);
    border-radius: 18px;
    overflow: hidden;
    box-shadow: 0 10px 28px rgba(0,0,0,.18);
  }
  .card--front { top: 50px; }
  .card--back { top: 500px; }

  .brand { display: flex; align-items: center; gap: 12px; }
  .brand__dot { width: 30px; height: 30px; border-radius: 50%; background: var(--yellow); flex: none; }
  .brand__name { font-weight: 800; color: var(--ink); letter-spacing: .04em; line-height: 1; white-space: nowrap; }
  .brand__sub { font-size: 11px; color: var(--ink); letter-spacing: .08em; text-transform: uppercase; margin-top: 5px; line-height: 1.3; white-space: nowrap; }

  .card--front .brand { position: absolute; left: 50%; top: 50%; transform: translate(-50%, -50%); }
  .card--front .brand__name { font-size: 30px; }

  .social { position: absolute; right: 34px; bottom: 30px; display: flex; align-items: center; gap: 16px; }
  .social__label { font-size: 15px; color: var(--muted); }
  .social__dot { width: 14px; height: 14px; border-radius: 50%; background: var(--muted); }
  .front-edge { position: absolute; left: 0; right: 0; bottom: 0; height: 8px; background: var(--navy); }

  .back__header { height: 150px; position: relative; padding: 34px 40px 0 40px; }
  .card--back .brand__name { font-size: 24px; }
  .holder { position: absolute; left: 40px; bottom: 20px; display: flex; align-items: center; gap: 10px; color: var(--ink); }
  .holder__name { font-size: 20px; letter-spacing: .06em; }
  .holder__role { font-size: 17px; color: var(--muted); margin-left: 22px; letter-spacing: .05em; }
  .holder svg { width: 18px; height: 18px; fill: var(--ink); }

  .back__panel { position: absolute; left: 0; right: 0; top: 150px; bottom: 0; background: var(--navy); }
  .accent-bar { position: absolute; left: 0; top: 0; bottom: 0; width: 46px; background: var(--yellow); }
  .contact { position: absolute; left: 90px; top: 26px; list-style: none; color: var(--light); }
  .contact li { display: flex; align-items: center; gap: 22px; font-size: 22px; letter-spacing: .05em; height: 50px; white-space: nowrap; }
  .contact li.contact__web { font-size: 18px; }
  .contact li.contact__address { align-items: flex-start; font-size: 20px; line-height: 1.2; padding-top: 8px; }
  .contact svg { width: 24px; height: 24px; fill: var(--light); flex: none; }
</style>
</head>
<body>

<section class="card card--front" aria-label="Card front">
  <div class="brand">
    <span class="brand__dot"></span>
    <div>
      <div class="brand__name">KEYSTONE</div>
      <div class="brand__sub">Property Maintenance<br>Harlow Falls, MA</div>
    </div>
  </div>
  <div class="social">
    <span class="social__label">like</span>
    <span class="social__dot"></span>
    <span class="social__dot"></span>
    <span class="social__dot"></span>
  </div>
  <div class="front-edge"></div>
</section>

<section class="card card--back" aria-label="Card back">
  <header class="back__header">
    <div class="brand">
      <span class="brand__dot"></span>
      <div>
        <div class="brand__name">KEYSTONE</div>
        <div class="brand__sub">Property Maintenance<br>Harlow Falls, MA</div>
      </div>
    </div>
    <div class="holder">
      <svg viewBox="0 0 24 24"><circle cx="12" cy="7" r="5"/><path d="M2 23c0-6 4.5-9 10-9s10 3 10 9z"/></svg>
      <span class="holder__name">DANIEL PRICE</span>
      <span class="holder__role">founder</span>
    </div>
  </header>
  <div class="back__panel">
    <div class="accent-bar"></div>
    <ul class="contact">
      <li>
        <svg viewBox="0 0 24 24"><path d="M6.6 2.5l3 3.6-2 2.4a13 13 0 0 0 7.9 7.9l2.4-2 3.6 3-1.8 3.6C11 20.8 3.2 13 3 4.3z"/></svg>
        <span>978 552 3716</span>
      </li>
      <li>
        <svg viewBox="0 0 24 24"><path d="M2 5h20v14H2z M3.5 6.5v.6L12 13l8.5-5.9v-.6z" fill-rule="evenodd"/></svg>
        <span>hello@keystonepm.com</span>
      </li>
      <li class="contact__web">
        <svg viewBox="0 0 24 24"><circle cx="12" cy="12" r="10" fill="none" stroke="#fff" stroke-width="2"/><path d="M2 12h20M12 2c-4 4-4 16 0 20M12 2c4 4 4 16 0 20M4 7h16M4 17h16" fill="none" stroke="#fff" stroke-width="1.5"/></svg>
        <span>www.keystonepm.com</span>
      </li>
      <li class="contact__address">
        <svg viewBox="0 0 24 24"><path d="M12 1a8 8 0 0 0-8 8c0 6 8 14 8 14s8-8 8-14a8 8 0 0 0-8-8zm0 11a3 3 0 1 1 0-6 3 3 0 0 1 0 6z"/></svg>
        <span>47 Brindlewood Rd.<br>Harlow Falls, MA 01839</span>
      </li>
    </ul>
  </div>
</section>

</body>
</html>
```